HomeBridle business card and stationary design

We are looking for a simple yet elegant design for our mortgage company business card and stationary.

The card should include:
Name (Derek Walsh)
Title (CEO)
Phone Number (614-208-3917)
Address (48 Birchfield Court, Suite 314, Marlow, OH 43952)
Email (email@homebridle-example.com)
"NMLS" i.e. (NMLS 61947)
"Company NMLS" (Company NMLS 472815)

See above

```html
<!DOCTYPE html>
<html lang="en">
<head>
<meta charset="utf-8">
<title>HomeBridle Business Card</title>
<link href="https://fonts.googleapis.com/css2?family=Montserrat:wght@500;700&family=Arimo:wght@400;700&display=swap" rel="stylesheet">
<style>
  :root {
    --navy: #1a2532;
    --sky: #29abe2;
    --white: #ffffff;
    --backdrop: #c9c9c9;
  }
  * { box-sizing: border-box; margin: 0; padding: 0; }
  html, body { width: 1200px; height: 788px; overflow: hidden; }
  body {
    background: var(--backdrop);
    display: flex;
    align-items: center;
    justify-content: center;
    gap: 40px;
    font-family: "Arimo", Arial, sans-serif;
  }
  .card {
    position: relative;
    width: 540px;
    height: 309px;
    border-radius: 22px;
    background: var(--navy);
    overflow: hidden;
    box-shadow: 0 10px 24px rgba(0,0,0,0.28);
  }
  .card__band { position: absolute; inset: 0; width: 100%; height: 100%; }
  .wordmark {
    font-family: "Montserrat", Arial, sans-serif;
    font-weight: 500;
    color: var(--white);
    letter-spacing: 0.5px;
    line-height: 1;
  }
  .front .wordmark { position: absolute; left: 30px; top: 78px; font-size: 40px; }
  .contact {
    position: absolute;
    right: 30px;
    top: 74px;
    text-align: right;
    color: var(--white);
  }
  .contact__name {
    font-family: "Montserrat", Arial, sans-serif;
    font-weight: 700;
    font-size: 19px;
    letter-spacing: 0.5px;
  }
  .contact__title { font-size: 12px; margin-top: 2px; }
  .contact__rule { width: 34px; height: 1px; background: var(--white); margin: 7px 0 8px auto; }
  .contact__line {
    display: flex;
    justify-content: flex-end;
    align-items: center;
    gap: 6px;
    font-size: 11.5px;
    line-height: 17px;
  }
  .contact__line svg { width: 11px; height: 11px; flex: none; }
  .address {
    position: absolute;
    left: 175px;
    bottom: 26px;
    color: var(--white);
    font-size: 12px;
    line-height: 17px;
  }
  .back { display: flex; align-items: center; justify-content: center; }
  .back .wordmark { font-size: 60px; }
</style>
</head>
<body>
  <article class="card front">
    <svg class="card__band" viewBox="0 0 540 309" preserveAspectRatio="none" aria-hidden="true">
      <polygon points="540,56 440,56 30,309 540,309" fill="var(--sky)"/>
    </svg>
    <div class="wordmark">HomeBridle</div>
    <div class="contact">
      <div class="contact__name">DEREK WALSH</div>
      <div class="contact__title">CEO</div>
      <div class="contact__rule"></div>
      <div class="contact__line"><span>NMLS 61947</span><svg viewBox="0 0 12 12"></svg></div>
      <div class="contact__line"><span>614-208-3917</span>
        <svg viewBox="0 0 12 12" aria-hidden="true"><path d="M2.5 1.5 L4.5 1.5 L5.2 4 L4 5 Q5 7.2 7 8 L8 6.8 L10.5 7.5 L10.5 9.5 Q10.5 10.5 9.5 10.5 Q2 10 1.5 2.5 Q1.5 1.5 2.5 1.5 Z" fill="var(--white)"/></svg>
      </div>
      <div class="contact__line"><span>email@homebridle-example.com</span>
        <svg viewBox="0 0 12 12" aria-hidden="true"><rect x="1" y="2.5" width="10" height="7" fill="var(--white)"/><path d="M1 2.5 L6 6.5 L11 2.5" fill="none" stroke="var(--sky)" stroke-width="1"/></svg>
      </div>
      <div class="contact__line"><span>www.homebridle.com</span>
        <svg viewBox="0 0 12 12" aria-hidden="true"><circle cx="6" cy="6" r="5" fill="var(--white)"/><path d="M1 6 H11 M6 1 Q3 6 6 11 M6 1 Q9 6 6 11" fill="none" stroke="var(--sky)" stroke-width="0.8"/></svg>
      </div>
    </div>
    <div class="address">
      48 Birchfield Court, Suite<br>
      314, Marlow, OH 43952<br>
      Company NMLS 472815
    </div>
  </article>

  <article class="card back">
    <div class="wordmark">HomeBridle</div>
  </article>
</body>
</html>
```